Hi,
We are start-up on a wild and crazy mission to change the world around us, cliche I know. We are currently developing passive emotional recognition software that will enable our environments to understand and respond to human emotion. What if our cars, homes, mobile phones, etc could augment their behavior and experience based on our emotional state.
We would like to improve the design and "wow" factor of our investor pitch deck. We have the majority of the content finished and now need to complete/improve the design. We have two more financial slides to come but I would like to get the design process started now.
We are looking for a simple, clean, and colorful (within reason) design. We want something that is in line with emotional colors - happy and engaging yet professional, if that is possible.
I look forward to your thoughts.
Industry/Entity Type
Software

```html
<!DOCTYPE html>
<html lang="en">
<head>
<meta charset="utf-8">
<title>Feelwave – Investor Deck</title>
<link rel="stylesheet" href="https://fonts.googleapis.com/css2?family=Open+Sans:wght@400;600;700&family=Signika:wght@600;700&display=swap">
<style>
  :root{
    --stage:#1b1b1b;
    --slide-top:#f4f4f4;
    --slide-bottom:#dcdcdc;
    --brand-blue:#1d4fae;
    --rule-blue:#2a66c4;
    --title-red:#8a1a1a;
    --pill-red:#c62a36;
    --accent-green:#36b82a;
    --body-grey:#555;
    --corner-sky:#6cc4ec;
    --corner-red:#c8283a;
    --corner-navy:#2b3990;
    --arrow-orange:#f39a1e;
    --algo-green:#9bd21e;
  }
  *{box-sizing:border-box;margin:0;padding:0}
  html,body{width:1200px;height:1000px;overflow:hidden;background:var(--stage)}
  body{position:relative;font-family:"Open Sans",Arial,sans-serif;color:var(--body-grey)}

  .slide{position:absolute;width:474px;height:352px;overflow:hidden;
    background:linear-gradient(160deg,var(--slide-top) 0%,#ebebeb 55%,var(--slide-bottom) 100%)}
  .slide::before{content:"";position:absolute;left:20px;right:20px;top:26px;height:2px;background:var(--rule-blue)}
  .slide::after{content:"";position:absolute;left:20px;right:150px;bottom:10px;height:2px;background:var(--rule-blue)}
  .slide-intro{left:14px;top:278px}
  .slide-what{left:711px;top:278px}
  .slide-team{left:14px;top:633px}
  .slide-how{left:711px;top:633px}

  .brand{font-family:"Signika",sans-serif;font-weight:700;color:var(--brand-blue);letter-spacing:-.5px}
  .brand-corner{position:absolute;right:22px;top:6px;font-size:19px}
  .corner-art{position:absolute;right:0;bottom:2px;width:140px;height:84px;border-radius:42px 0 0 42px;
    background:linear-gradient(180deg,var(--corner-sky) 0%,var(--corner-red) 50%,var(--corner-navy) 100%)}
  .slide-num{position:absolute;right:40px;bottom:14px;font-weight:700;font-size:38px;line-height:44px;color:#fff}

  .pill{position:absolute;left:30px;top:38px;height:28px;padding:0 28px 0 12px;border-radius:14px;
    background:var(--pill-red);color:#fff;font-weight:700;font-size:19px;line-height:28px}

  /* cover */
  .cover{position:absolute;left:441px;top:2px;width:346px;height:260px;overflow:hidden;
    background:radial-gradient(ellipse at 60% 45%,#f4f8fd 0%,#cfe2f7 60%,#b4d2f2 100%)}
  .cover-brand{position:absolute;left:0;right:0;top:78px;text-align:center;font-size:36px}
  .cover .corner-art{width:104px;height:62px;border-radius:31px 0 0 31px}

  /* intro */
  .intro-brand{position:absolute;left:34px;top:32px;font-size:40px}
  .intro-tag{position:absolute;left:34px;top:84px;font-weight:700;font-size:14px;line-height:17px;color:var(--title-red)}
  .intro-body{position:absolute;left:34px;top:130px;width:256px;font-size:10px;line-height:13px;text-align:justify;letter-spacing:.2px}
  .intro-body p+p{margin-top:4px}
  .hl{color:var(--accent-green);font-weight:700}
  .hl-i{color:var(--accent-green);font-weight:700;font-style:italic}
  .intro-art{position:absolute;left:316px;top:80px;width:138px;height:139px;background:#fbd97a}
  .intro-question{position:absolute;left:30px;top:286px;width:300px;font-size:10.5px;line-height:13px;text-align:center}

  /* what */
  .what-body{position:absolute;left:28px;top:100px;width:398px;font-size:10.8px;line-height:13.5px;text-align:justify;letter-spacing:.2px}
  .what-body p+p{margin-top:5px}
  .what-body .brand{font-size:18px}

  /* team */
  .member{position:absolute;font-size:8.5px;line-height:10.5px;color:#777}
  .member-name{color:var(--title-red);font-weight:700}
  .photo{position:absolute;background:linear-gradient(160deg,#8a8a8a,#3c3c3c)}
  .photo-bar{position:absolute;width:5px;background:var(--accent-green)}

  /* how */
  .slide-how .pill{font-size:15px}
  .diagram{position:absolute;inset:0;width:474px;height:352px}
  .label{position:absolute;font-size:8.5px;color:var(--title-red);text-transform:uppercase}
  .list{position:absolute;font-size:8.5px;line-height:10.5px;color:#333;text-align:center}
</style>
</head>
<body>

<section class="cover">
  <div class="brand cover-brand">Feelwave</div>
  <div class="corner-art" role="img" aria-label="Decorative corner motif of stacked colour bands"></div>
</section>

<section class="slide slide-intro">
  <div class="brand brand-corner">Feelwave</div>
  <div class="brand intro-brand">Feelwave</div>
  <h2 class="intro-tag">Enabling Technology to<br>Quantify Human Emotion</h2>
  <div class="intro-body">
    <p>Technology doesn't <span class="hl">understand</span> mobile users circumstances (emotions and context).</p>
    <p>This is recognised as an immediate and pervasive problem in the mobile world as it creates huge inefficiencies in the way brands, app developers, and service providers engage with their mobile customers.</p>
  </div>
  <div class="intro-art" role="img" aria-label="Illustration of connected smartphones surrounded by app and message icons"></div>
  <p class="intro-question">What if our technology was <span class="hl-i">emotionally and contextually aware</span> and could react and adapt accordingly?</p>
  <div class="corner-art" role="img" aria-label="Decorative corner motif of stacked colour bands"></div>
  <span class="slide-num">1</span>
</section>

<section class="slide slide-what">
  <div class="brand brand-corner">Feelwave</div>
  <h2 class="pill">What do we do?</h2>
  <div class="what-body">
    <p><span class="brand">Feelwave</span> is developing incredible technology that will enable our smart devices to <span class="hl-i">adapt and react to user's circumstances</span> (emotions &amp; context)</p>
    <p>Our patented-pending technology, in the form of an SDK, is embedded in the code of mobile applications. Running passively in the background, we utilise a gamut of sensors in a smart device to follow a mobile user's environment and behavioral patterns.</p>
    <p>From this we infer emotional states and historical trends that provide incredibly valuable analytics and actionable information for brands, apps, and service providers.</p>
  </div>
  <div class="corner-art" role="img" aria-label="Decorative corner motif of stacked colour bands"></div>
  <span class="slide-num">2</span>
</section>

<section class="slide slide-team">
  <div class="brand brand-corner">Feelwave</div>
  <h2 class="pill">The Team</h2>

  <div class="member" style="left:4px;top:106px;width:98px;text-align:right">
    <div class="member-name">Daniel Morrow (CEO)</div>
    Product Design and Innovation. Studied Computer Science and Neuroscience
  </div>
  <div class="photo" style="left:105px;top:88px;width:102px;height:100px" role="img" aria-label="Portrait photo of the CEO"></div>
  <div class="photo-bar" style="left:207px;top:88px;height:100px"></div>

  <div class="member" style="left:214px;top:68px;width:116px;text-align:right">
    <div class="member-name">Lukas Brenner<br>(Chief Data Scientist)</div>
    Product Design and Implementation. Scientific work published in Journal of Brain Studies.
  </div>
  <div class="photo" style="left:338px;top:50px;width:106px;height:100px" role="img" aria-label="Portrait photo of the Chief Data Scientist"></div>
  <div class="photo-bar" style="left:447px;top:50px;height:100px"></div>

  <div class="member" style="left:216px;top:172px;width:110px;text-align:right">
    <div class="member-name">Sam Whitley (COO).</div>
    Business Development and Operations. Masters of Commerce. Third start up.
  </div>
  <div class="photo" style="left:330px;top:163px;width:103px;height:97px" role="img" aria-label="Portrait photo of the COO"></div>
  <div class="photo-bar" style="left:435px;top:163px;height:97px"></div>

  <div class="member" style="left:18px;top:246px;width:100px;text-align:right">
    <div class="member-name">Clara Jensen</div>
    Lead Software Engineer. Master of Computer Science.
  </div>
  <div class="photo" style="left:122px;top:228px;width:105px;height:100px" role="img" aria-label="Portrait photo of the Lead Software Engineer"></div>
  <div class="photo-bar" style="left:228px;top:228px;height:100px"></div>

  <div class="corner-art" role="img" aria-label="Decorative corner motif of stacked colour bands"></div>
  <span class="slide-num">3</span>
</section>

<section class="slide slide-how">
  <div class="brand brand-corner">Feelwave</div>
  <h2 class="pill">How Feelwave works</h2>

  <svg class="diagram" viewBox="0 0 474 352" aria-hidden="true">
    <defs>
      <marker id="head" viewBox="0 0 10 10" refX="5" refY="5" markerWidth="3.2" markerHeight="3.2" orient="auto">
        <path d="M0 0 L10 5 L0 10 Z" fill="var(--arrow-orange)"/>
      </marker>
    </defs>
    <g fill="none" stroke="var(--arrow-orange)" stroke-width="5" marker-end="url(#head)">
      <path d="M120 122 H205"/>
      <path d="M320 92 Q365 92 365 140"/>
      <path d="M372 218 V248 Q372 262 342 262"/>
      <path d="M245 300 L205 278"/>
      <path d="M60 240 Q30 255 60 272"/>
      <path d="M175 290 Q205 262 178 235"/>
    </g>
    <path d="M288 180 V208 A45 8 0 0 0 378 208 V180" fill="#86bb14"/>
    <rect x="288" y="180" width="90" height="28" fill="var(--algo-green)"/>
    <ellipse cx="333" cy="180" rx="45" ry="8" fill="#c4ea5a"/>
    <text x="333" y="200" text-anchor="middle" font-family="Open Sans, sans-serif" font-size="14" fill="#fff">Algorithm</text>
  </svg>

  <div class="label" style="left:22px;top:76px">Smart phone inputs</div>
  <div class="list" style="left:30px;top:96px;width:100px">GPS<br>Accelerometer<br>Local Weather<br>Ambient Light Sensor<br>Microphone<br>Social Activity<br>Time &amp; Date</div>

  <div class="label" style="left:220px;top:84px">Action points</div>
  <div class="list" style="left:200px;top:106px;width:110px">Sleep pattern<br>Work pattern<br>Home patterns<br>Exercise patterns<br>Commute/Travel Patterns</div>

  <div class="label" style="left:236px;top:236px;width:80px;text-align:center">Emotive values<br>(context)</div>
  <div class="list" style="left:250px;top:272px;width:60px">Time<br>Location<br>Happy/Sad<br>Irritable<br>Stressed<br>Fatigued</div>

  <div class="list" style="left:70px;top:186px;width:100px">Real-time Actionable information: i.e. mood-based advertising or service augmentation</div>
  <div class="list" style="left:70px;top:258px;width:100px">Insight's and predicative analytics: i.e. when to engage with mobile user's at the most receptive times.</div>

  <div class="corner-art" role="img" aria-label="Decorative corner motif of stacked colour bands"></div>
  <span class="slide-num">4</span>
</section>

</body>
</html>
```